Litigation Support Company Needing new Simple Web Design

I need to re-design a self done wix hosted website for a small yet nation-wide litigation support consulting firm. I built mine at www.brief-tracer.com myself when I launched but it is very hard on the eyes and needs refreshing/updates. Thanks for taking a look!

Target Market(s)

Law firms and technology experts in the litigation support field.

Number of Pages Required

4 page

Font styles to use
Serif

Colors
f78f20
faa54b
fac994

Requirements
Must have
• Blog, About Us, Services Pages, Crisper Graphics etc.

```html
<!DOCTYPE html>
<html lang="en">
<head>
<meta charset="utf-8">
<title>BriefTracer – Litigation Support</title>
<link rel="stylesheet" href="https://fonts.googleapis.com/css2?family=Lato:wght@400;700;900&family=Montserrat:wght@400;600;700&family=Oswald:wght@400;500&display=swap">
<style>
:root{
  --orange:#f4622a;
  --orange-soft:#faa54b;
  --ink:#222;
  --text:#555;
  --muted:#999;
  --line:#e6e6e6;
  --bg-soft:#f4f4f4;
  --dark:#333;
  --white:#fff;
}
*{margin:0;padding:0;box-sizing:border-box}
html,body{width:1200px;height:3455px;overflow:hidden}
body{font-family:"Lato",sans-serif;color:var(--ink);background:var(--white);position:relative}
.abs{position:absolute}
.brand{font-family:"Lato",sans-serif;font-weight:700;color:var(--ink);display:flex;align-items:center;gap:8px}
.brand .dot{width:14px;height:14px;border-radius:50%;background:var(--orange)}
/* header */
.site-header{left:0;top:0;width:1200px;height:104px;background:var(--white)}
.site-header .brand{left:120px;top:30px;font-size:36px}
.nav{right:118px;top:44px;display:flex;gap:34px;font-family:"Montserrat",sans-serif;font-size:12px;font-weight:600;letter-spacing:.3px}
.nav a{color:#333;text-decoration:none}
.nav a.active{color:var(--orange)}
/* hero */
.hero{left:0;top:104px;width:1200px;height:481px;background:linear-gradient(120deg,#3c4650 0%,#6a7884 45%,#9aa7b0 75%,#cfd6da 100%)}
.hero-author{left:120px;top:82px;font-family:"Montserrat",sans-serif;font-weight:700;font-size:16px;color:var(--white)}
.hero-title{left:118px;top:116px;width:440px;font-family:"Montserrat",sans-serif;font-weight:700;font-size:40px;line-height:48px;color:var(--white)}
.hero-lead{left:120px;top:284px;width:330px;font-size:15px;line-height:19px;color:var(--white)}
.btn-primary{left:122px;top:363px;width:253px;height:42px;border-radius:21px;background:var(--orange);color:var(--white);font-family:"Montserrat",sans-serif;font-weight:700;font-size:13px;display:flex;align-items:center;justify-content:center;gap:14px}
.hero-arrow{top:190px}
.hero-dots{left:568px;top:428px;display:flex;gap:8px}
.hero-dots span{width:11px;height:11px;border:2px solid var(--white);transform:rotate(45deg)}
.hero-dots span.on{background:var(--white)}
/* section headings */
.sec-title{left:0;width:1200px;text-align:center;font-family:"Oswald",sans-serif;font-weight:500;font-size:31px;color:var(--ink)}
.sec-sub{left:300px;width:600px;text-align:center;font-size:14px;line-height:19px;color:var(--muted)}
.sec-sub.dark{color:#333}
/* services */
.service-card{background:var(--white);box-shadow:0 2px 10px rgba(0,0,0,.06)}
.service-card.raised{box-shadow:0 6px 22px rgba(0,0,0,.18)}
.service-img{position:absolute;left:0;top:0;width:100%;height:168px}
.service-card h3{position:absolute;left:36px;top:194px;width:220px;font-size:16px;font-weight:700;line-height:21px}
.service-card p{position:absolute;left:36px;top:246px;width:250px;font-size:13px;line-height:18px;color:var(--muted)}
.btn-outline{position:absolute;border:1.5px solid #555;border-radius:16px;font-family:"Montserrat",sans-serif;font-size:9px;font-weight:600;display:flex;align-items:center;justify-content:center;color:#333}
/* about */
.about-band{left:0;top:1220px;width:1200px;height:620px;background:var(--bg-soft)}
.about-panel{left:479px;top:1264px;width:721px;height:459px;background:var(--orange)}
.about-photo{left:120px;top:1320px;width:430px;height:352px;background:linear-gradient(135deg,#e9ecef,#bfc6cc 60%,#5d6772)}
.about-title{left:634px;top:1340px;font-family:"Oswald",sans-serif;font-size:31px;color:var(--white)}
.about-rule{left:634px;top:1396px;width:446px;height:3px;background:var(--white)}
.about-quote{left:634px;top:1420px;width:430px;font-size:21px;line-height:26px;color:var(--white)}
.about-text{left:634px;top:1514px;width:450px;font-size:14px;line-height:23px;color:#ffd9c6}
.about-panel-btn{left:634px;top:1617px;width:108px;height:30px;border-color:var(--white);color:var(--white)}
/* contact */
.field{background:var(--white);box-shadow:0 1px 8px rgba(0,0,0,.12);display:flex;align-items:center;gap:10px;padding-left:18px;font-size:12px;color:#666}
.field.msg{align-items:flex-start;padding-top:14px}
.btn-dark{left:507px;top:2262px;width:186px;height:42px;border-radius:21px;background:#444;color:var(--white);font-family:"Montserrat",sans-serif;font-weight:700;font-size:13px;display:flex;align-items:center;justify-content:center}
/* blog */
.blog-band{left:0;top:2395px;width:1200px;height:702px;background:var(--bg-soft)}
.post{background:var(--white);width:467px;height:189px}
.post-thumb{position:absolute;left:0;top:0;width:180px;height:189px;display:flex;align-items:center;justify-content:center}
.post-meta{position:absolute;left:209px;top:24px;width:220px;font-size:11px;color:#777;padding-bottom:10px;border-bottom:1px solid var(--line)}
.post-title{position:absolute;left:209px;top:66px;width:220px;font-size:17px;line-height:22px;font-weight:700;color:var(--ink)}
.post-title.link{color:var(--orange);text-decoration:underline;width:215px}
/* footer */
.site-footer{left:0;top:3097px;width:1200px;height:358px;background:var(--dark);color:#ddd}
.foot-col{top:90px;font-size:11px;line-height:18px}
.foot-col h4{font-size:11px;font-weight:700;color:var(--white);margin-bottom:14px}
.foot-col li{list-style:none}
.foot-col li::before{content:"› ";color:#aaa}
.contact-row{display:flex;align-items:center;gap:12px;margin-bottom:16px}
.social{left:958px;top:108px;display:flex;gap:8px}
.social span{width:24px;height:24px;border:1.5px solid #ddd;border-radius:50%}
.foot-rule{left:339px;top:261px;width:520px;height:1px;background:#666}
.site-footer .brand{left:0;width:1200px;justify-content:center;top:290px;font-size:22px;color:var(--white)}
</style>
</head>
<body>

<header class="site-header abs">
  <div class="brand abs"><span class="dot"></span>BriefTracer</div>
  <nav class="nav abs">
    <a class="active" href="#">HOME</a><a href="#">SERVICES</a><a href="#">ABOUT US</a><a href="#">CONTACT</a><a href="#">BRIEF-TRACER BLOG</a>
  </nav>
</header>

<section class="hero abs" role="img" aria-label="Analyst reviewing documents on computer monitors">
  <div class="hero-author abs">Dan Reyes</div>
  <h1 class="hero-title abs">Don't just review investigate and discover</h1>
  <p class="hero-lead abs">Lorem ipsum dolor sit amet, consectetur adipisicing elit, sed do eiusmod tempor incididunt ut labore et dolore magna aliqua. Ut</p>
  <div class="btn-primary abs">GET STARTED NOW
    <svg width="10" height="14" viewBox="0 0 10 14"><path d="M2 1l6 6-6 6" stroke="#fff" stroke-width="2.5" fill="none"/></svg></div>
  <svg class="hero-arrow abs" style="left:52px" width="18" height="32" viewBox="0 0 18 32"><path d="M16 2L3 16l13 14" stroke="#fff" stroke-width="2.5" fill="none"/></svg>
  <svg class="hero-arrow abs" style="left:1080px" width="18" height="32" viewBox="0 0 18 32"><path d="M2 2l13 14L2 30" stroke="#fff" stroke-width="2.5" fill="none"/></svg>
  <div class="hero-dots abs"><span></span><span class="on"></span><span></span></div>
</section>

<h2 class="sec-title abs" style="top:658px">Our Services</h2>
<p class="sec-sub abs" style="top:716px">Lorem ipsum dolor sit amet, consectetur adipisicing elit, sed do eiusmod tempor incididunt ut labore et dolore magna aliqua. Ut enim ad minim veniam</p>

<article class="service-card abs" style="left:120px;top:815px;width:313px;height:348px">
  <div class="service-img" role="img" aria-label="Magnifying glass over code on a screen" style="background:linear-gradient(135deg,#1c2a3a,#55677a)"></div>
  <h3>Received Data Discovery Review Management</h3>
  <p>Lorem ipsum dolor sit amet, elit, sed do eiusmod tempor labore dolore</p>
  <div class="btn-outline" style="left:36px;top:312px;width:108px;height:28px">LEARN MORE</div>
</article>
<article class="service-card raised abs" style="left:433px;top:800px;width:336px;height:377px">
  <div class="service-img" role="img" aria-label="Judge's gavel on a desk" style="height:184px;background:linear-gradient(135deg,#2c2620,#8a7a68 60%,#cfc6ba)"></div>
  <h3 style="top:208px;left:42px">BriefTracer Managed Litigation Support</h3>
  <p style="top:260px;left:42px">Lorem ipsum dolor sit amet, elit, do eiusmod tempor labore</p>
  <div class="btn-outline" style="left:42px;top:326px;width:108px;height:28px">LEARN MORE</div>
</article>
<article class="service-card abs" style="left:769px;top:815px;width:311px;height:348px">
  <div class="service-img" role="img" aria-label="Team celebrating around a meeting table" style="background:linear-gradient(135deg,#d8d4cf,#a89b8e 55%,#5a4e44)"></div>
  <h3 style="left:26px">Pre-Discovery Strategy and Support Services</h3>
  <p style="left:26px">Lorem ipsum dolor sit amet, elit, do eiusmod tempor labore</p>
  <div class="btn-outline" style="left:26px;top:312px;width:108px;height:28px">LEARN MORE</div>
</article>

<div class="about-band abs"></div>
<div class="about-panel abs"></div>
<div class="about-photo abs" role="img" aria-label="Portrait of the company's CEO in a suit"></div>
<h2 class="about-title abs">ABOUT DAN the CEO</h2>
<div class="about-rule abs"></div>
<p class="about-quote abs">I believe that proper application of technology can make or break the discovery process of small and large matters alike.</p>
<p class="about-text abs">Document review projects can create endless headaches without proper strategy and it is my goal to analyze every project individually and apply the proper level of technology to fit the client's needs.</p>
<div class="btn-outline about-panel-btn abs">LEARN MORE</div>

<h2 class="sec-title abs" style="top:1910px">Contact Us</h2>
<p class="sec-sub dark abs" style="top:1968px">Lorem ipsum dolor sit amet, consectetur adipisicing elit, sed do eiusmod tempor incididunt ut labore et dolore magna aliqua. Ut enim ad minim veniam</p>
<div class="field abs" style="left:281px;top:2038px;width:313px;height:42px">
  <svg width="16" height="16" viewBox="0 0 16 16"><circle cx="8" cy="8" r="6.5" stroke="#999" fill="none"/><circle cx="8" cy="6.5" r="2.2" stroke="#999" fill="none"/><path d="M4 12.5c1-2 7-2 8 0" stroke="#999" fill="none"/></svg>Your Name</div>
<div class="field abs" style="left:603px;top:2038px;width:314px;height:42px">
  <svg width="16" height="12" viewBox="0 0 16 12"><rect x=".5" y=".5" width="15" height="11" stroke="#999" fill="none"/><path d="M1 1l7 6 7-6" stroke="#999" fill="none"/></svg>Email</div>
<div class="field msg abs" style="left:281px;top:2093px;width:636px;height:116px">
  <svg width="16" height="14" viewBox="0 0 16 14"><path d="M1 1h14v9H6l-3 3v-3H1z" stroke="#999" fill="none"/></svg>Message</div>
<div class="btn-dark abs">SEND MESSAGE</div>

<div class="blog-band abs"></div>
<h2 class="sec-title abs" style="top:2456px">Latest Blog</h2>
<p class="sec-sub abs" style="top:2508px">Lorem ipsum dolor sit amet, consectetur adipisicing elit, sed do eiusmod tempor incididunt ut labore et dolore magna aliqua. Ut enim ad minim veniam</p>

<article class="post abs" style="left:120px;top:2593px">
  <div class="post-thumb" role="img" aria-label="Laptop and glasses on a desk" style="background:linear-gradient(135deg,#f1f1f1,#c9ccd0 60%,#7d858c)"></div>
  <div class="post-meta">01 SEP 2018 &nbsp;|&nbsp; BY DAN REYES</div>
  <div class="post-title link">Knowledge is power. Certainly an overused expression in all walks of life, but it still rings truer than</div>
</article>
<article class="post abs" style="left:613px;top:2593px">
  <div class="post-thumb"><span class="brand" style="font-size:24px">Nuvalo</span></div>
  <div class="post-meta">01 SEP 2018 &nbsp;|&nbsp; BY DAN REYES</div>
  <div class="post-title">Blog text for brief-tracer lorem dolor sit amet, elit, do eiusmod tempor ut labore et dolore</div>
</article>
<article class="post abs" style="left:120px;top:2807px">
  <div class="post-thumb"><span class="brand" style="font-size:19px"><span class="dot" style="width:9px;height:9px"></span>BriefTracer</span></div>
  <div class="post-meta">01 SEP 2018 &nbsp;|&nbsp; BY DAN REYES</div>
  <div class="post-title">Blog text for brief-tracer lorem dolor sit amet, elit, do eiusmod tempor ut labore et dolore</div>
</article>
<article class="post abs" style="left:613px;top:2807px">
  <div class="post-thumb"><span class="brand" style="font-size:19px"><span class="dot" style="width:9px;height:9px"></span>BriefTracer</span></div>
  <div class="post-meta">01 SEP 2018 &nbsp;|&nbsp; BY DAN REYES</div>
  <div class="post-title">Blog text for brief-tracer lorem dolor sit amet, elit, do eiusmod tempor ut labore et dolore</div>
</article>

<footer class="site-footer abs">
  <div class="foot-col abs" style="left:120px"><h4>Getting Started</h4>
    <ul><li>Home</li><li>About Us</li><li>Services</li><li>Blog</li><li>Contact Us</li></ul></div>
  <div class="foot-col abs" style="left:311px"><h4>Specialties</h4>
    <ul><li>Received Data Discovery Review Management</li><li>Managed Litigation Support</li><li>Pre-Discovery Strategy and Support Services</li></ul></div>
  <div class="foot-col abs" style="left:661px"><h4>Contact Us</h4>
    <div class="contact-row"><svg width="10" height="14" viewBox="0 0 10 14"><path d="M5 13S1 8 1 5a4 4 0 018 0c0 3-4 8-4 8z" fill="#ddd"/><circle cx="5" cy="5" r="1.5" fill="#333"/></svg><span>Lorem Ipsum Address<br>4100 Harlow</span></div>
    <div class="contact-row"><svg width="12" height="12" viewBox="0 0 12 12"><path d="M2 1l2.5 0 1 3-1.5 1c.8 1.6 1.4 2.2 3 3l1-1.5 3 1V11C6 11 1 6 1 2z" fill="#ddd"/></svg><span>(555)014-2290</span></div>
    <div class="contact-row"><svg width="12" height="9" viewBox="0 0 12 9"><rect width="12" height="9" fill="#ddd"/><path d="M0 0l6 5 6-5" stroke="#333" fill="none"/></svg><span>info@brief-tracer.com</span></div>
  </div>
  <div class="foot-col abs" style="left:887px;top:84px">© 2018 &nbsp;brief-tracer Legal &amp; Privacy</div>
  <div class="social abs"><span></span><span></span><span></span><span></span></div>
  <div class="foot-rule abs"></div>
  <div class="brand abs"><span class="dot" style="width:10px;height:10px"></span>BriefTracer</div>
</footer>

</body>
</html>
```